Remote Game Console (Vexlar) Wpf/Web UI

A complete interface for a second generation remote console tool to administer PC games. Will primarily run as a desktop application with future plans of running within a browser.

All materials are supplied as a guide only, but the designer is free to build what they would find easy to use. We're engineers so help us out with a good user experience.

The first version of Vexlar Tidewell was released in March 2009 supporting Skirmline: Rust Brigade 2. It was updated later in the year to support the expansion, SLRB2: Kestova. Ember Sigil followed in late 2010 and Skirmline 3 support in October 2011. All games are based on MORB's Tidewell engine. http://quarnix.example/vexlar-tidewell/

Vexlar 2 will eventually support all games, working more along the lines of a framework for others to expand upon. While ultimately having a similar function as Vexlar Tidewell, Vexlar 2 has been completely rewritten and shares no similarities internally.

The primary focus of the application is to display details about a users rented Game Server. A user can kick, ban and chat with players in their servers. A user can alter the settings of their game server, setting the time of a round or the game servers name for instance.

We have a forum dedicated to this competition that users of our software can give general feedback about the existing (Vexlar Tidewell) software, such as what they hate etc. http://www.quarnix.example/forumvb/forumdisplay.php?35-UI-Competition

You can find similar software with much cooler looking UI's at http://www.rb2hq.example/ and http://sl3hq.example/

The techy details:

Vexlar 2 can run locally or connect and login to a hosted version of the software (internally we call this a Local Interface or Remote Interface). Logging into a remote server requires an IP, port, username and password. Beyond the initial local/remote selection the UI can function identically.

1 Instance of the software has a single Local (no login required) or Remote (ip/port/username/password required) Interface.

1 Instance has many Packages. A package is an extension to the software that the user can install. A package can be an update to Vexlar 2 itself, a plugin or a config.

1 Instance has many Options. We are partial to Nimbex Orbits Options panel. Something similar which would allow us to expand would be neat.

1 Instance has many languages.

1 Interface has many Game Connections. A game connection requires an ip, port and password to connect and authenticate. A game connection has a name, maximum players allowed to connect, a game type (e.g rust brigade 2, ember sigil, skirmline 3).

1 Game Connection has many plugins. A plugin extends the functionality of the software in the background.

1 Game Connection has many players. A player has a name, country, score, ping, kills, deaths and other variables depending on the type of Game connected to.

1 Game Connection has many bans. A ban is a record of a player, the players identifying information, a small description of why the ban was put in place as well as an expiry time (e.g. banned for 2 weeks or permanently banned)

1 Game Connection has many settings. These settings can vary dramatically depending on the Game connected to.

1 Interface has many Groups. A group has a name any many permissions.

1 Group has many Accounts.

1 Account has many players.
Updates

Project Deadline Extended
Reason: Uploaded wireframes. I work a lot and this is my side project. I thought I would have wireframes the next day of this project, but it didn't end up like that. All current submissions have been the first iteration of my software reskinned, not the next version.

Target Market(s)

First Person Shooter PC game administrators

Industry/Entity Type

Software

Requirements
Must have
• Vexlar 2 has a primitive natural language parser for converting free text into commands for the program. An online functional example is available at http://labs.zentari.example/the-budget-oracle/ (check down the bottom). The design should incorporate a text box throughout the application for users to enter commands in. As the user types this could be passed to display what will happen once the user executes the command

Generally people will be minimizing their games to kick or ban people from their servers. The UI design should be easy enough to navigate quickly.

A UI that can handle multiple languages. Our primary market is Germany.

The UI must be usable at 1024x768. It should be designed to take up the maximum window/browser space.
Nice to have
• Responsive design that scales to any resolution. We have a large mobile user base that could benefit from a UI that scales well on lower resolutions.

Vexlar 2 has no set logo as of yet, though we will continue using the smiley found at http://quarnix.example - we only have a 100 by 100px png of this image though. If a larger version is supplied you'll receive a virtual cookie and a thank you! The logo will probably end up as a variation of that found on http://quarnix.example/vexlar-tidewell/ but we'll go through the exact process for this at a later date

```html
<!DOCTYPE html>
<html lang="en">
<head>
<meta charset="utf-8">
<title>Vexlar Tidewell – Events</title>
<link href="https://fonts.googleapis.com/css2?family=Arimo:wght@400;700&display=swap" rel="stylesheet">
<style>
:root{
  --page:#d9d9d9;
  --titlebar:#ececec;
  --shell:#141414;
  --tabbar:#0b0b0b;
  --tab-text:#f2f2f2;
  --accent:#e2301c;
  --content:#e3e3e3;
  --panel:#ffffff;
  --panel-head:#dcdcdc;
  --rule:#b9b9b9;
  --text:#333333;
  --muted:#5c5c5c;
  --ok:#3aa53a;
}
*{box-sizing:border-box;margin:0;padding:0}
html,body{width:1191px;height:1200px;overflow:hidden}
body{background:var(--page);font-family:"Arimo",Arial,sans-serif;color:var(--text);position:relative}
.abs{position:absolute}
.titlebar{left:0;top:0;width:1191px;height:46px;background:var(--titlebar)}
.app-title{left:72px;top:13px;font-size:16px;color:#222}
.app-dot{left:42px;top:13px;width:18px;height:18px;border-radius:50%;background:#2b2b2b;border:3px solid #777}
.win-controls{left:1003px;top:0;display:flex;gap:2px}
.win-controls span{display:block;width:30px;height:20px;background:#4a4a4a;border:1px solid #222;border-radius:2px}
.win-controls .close{width:48px;background:#555}
.shell{left:18px;top:46px;width:1162px;height:1098px;background:var(--shell)}
.hero{left:18px;top:46px;width:1162px;height:165px;background:linear-gradient(100deg,#1b1b1b 0%,#262626 35%,#3a3530 55%,#6b4a2a 78%,#2d231b 100%)}
.menu{left:48px;top:67px;display:flex;gap:30px;color:#fff;font-size:15px}
.server-select{left:238px;top:102px;width:542px;height:35px;background:#f4f4f4;border-radius:3px;font-size:11px;color:#444;display:flex;align-items:center;padding-left:10px;gap:10px}
.server-select .game{font-size:15px;color:#333;letter-spacing:-0.5px}
.auto-connect{left:852px;top:102px;width:225px;height:35px;background:#f4f4f4;border-radius:3px;font-size:11px;color:#555;display:flex;align-items:center;padding-left:18px;gap:12px}
.status-line{left:42px;top:173px;color:#fff;font-size:14px}
.status-red{color:var(--accent)}
.tabs{left:34px;top:211px;width:1134px;height:42px;background:var(--tabbar);display:flex}
.tabs span{color:var(--tab-text);font-size:14px;line-height:42px;padding:0 20px;border-right:1px solid #333}
.tabs .active{color:var(--accent)}
.content{left:34px;top:253px;width:1134px;height:863px;background:var(--content)}
.event-table{left:51px;top:270px;width:797px;height:820px;background:var(--panel);border:1px solid var(--rule)}
.thead{left:0;top:0;width:795px;height:42px;background:var(--panel-head);border-bottom:1px solid var(--rule)}
.col-line{top:0;width:1px;height:818px;background:var(--rule)}
.th{top:14px;font-size:14px;color:#333}
.row{left:0;width:795px;height:30.6px;font-size:13px;color:var(--muted)}
.row span{position:absolute;top:0}
.captures{left:865px;top:270px;width:290px;height:820px;background:var(--panel-head);border:1px solid var(--rule)}
.cap-head{left:0;top:0;width:288px;height:42px;font-size:14px;padding:13px 26px}
.cap-close{right:10px;top:9px;font-size:12px;color:var(--accent)}
.cap-label{left:26px;font-size:14px}
.field{left:26px;width:227px;height:37px;background:#fff;border:1px solid #aaa;border-radius:5px;font-size:14px;padding:10px 14px}
.list{left:26px;top:262px;width:227px;height:489px;background:#fff;border:1px solid #aaa;border-radius:5px;overflow:hidden}
.list .item{left:14px;font-size:14px;color:#444}
.vscroll{left:204px;top:0;width:21px;height:468px;background:#eee;border-left:1px solid #ccc}
.hscroll{left:0;top:468px;width:225px;height:19px;background:#eee;border-top:1px solid #ccc}
.btn{left:26px;top:764px;width:227px;height:37px;background:#fff;border:1px solid #aaa;border-radius:5px;font-size:14px;text-align:center;line-height:35px}
</style>
</head>
<body>
<div class="abs titlebar"></div>
<div class="abs app-dot"></div>
<div class="abs app-title">Vexlar Tidewell</div>
<div class="abs win-controls"><span></span><span></span><span></span><span></span><span class="close"></span></div>

<div class="abs shell"></div>
<div class="abs hero" role="img" aria-label="Dark in-game battle scene with a glowing explosion"></div>

<nav class="abs menu"><span>File</span><span>Tools</span><span>Help</span></nav>
<svg class="abs" style="left:44px;top:100px" width="140" height="34" viewBox="0 0 140 34" fill="#fff">
  <path d="M16 2 L30 15 H26 V28 H6 V15 H2 Z"/>
  <path d="M54 18 H80 V22 H54 Z M54 20 L64 10 L66 13 L59 20 L66 27 L64 30 Z"/>
  <path d="M104 18 H130 V22 H104 Z M132 20 L122 10 L120 13 L127 20 L120 27 L122 30 Z"/>
</svg>

<div class="abs server-select">
  <span class="game">Skirmline</span>
  <svg width="14" height="12" viewBox="0 0 14 12"><path d="M1 6 L5 10 L13 1" stroke="var(--ok)" stroke-width="2.5" fill="none"/></svg>
  <span>[ 32/32 ] Vexlar [gxnet.example - Deine Community! --&gt; www.gxnet.example] |</span>
  <svg style="position:absolute;right:12px;top:12px" width="14" height="10" viewBox="0 0 14 10"><path d="M1 1 L7 8 L13 1" stroke="#444" stroke-width="2.5" fill="none"/></svg>
</div>
<svg class="abs" style="left:808px;top:114px" width="16" height="16" viewBox="0 0 16 16"><path d="M3 12 L13 4 M5 6 L10 11" stroke="#bbb" stroke-width="2"/></svg>
<div class="abs auto-connect">
  <svg width="16" height="13" viewBox="0 0 14 12"><path d="M1 6 L5 10 L13 1" stroke="var(--ok)" stroke-width="2.5" fill="none"/></svg>
  <span>Automatically Connect</span>
</div>

<div class="abs status-line">Rush - Corvane Round : 1/2</div>
<svg class="abs" style="left:274px;top:162px" width="90" height="44" viewBox="0 0 90 44" fill="none" stroke="#fff" stroke-width="4">
  <path d="M20 6 A15 15 0 0 0 8 26"/><path d="M10 36 A15 15 0 0 0 22 16"/>
  <path d="M4 20 L8 28 L14 22" stroke-width="3"/><path d="M26 22 L22 14 L16 20" stroke-width="3"/>
  <path d="M64 14 A10 10 0 1 1 76 24"/><circle cx="70" cy="30" r="2" fill="#fff"/>
</svg>
<div class="abs status-line" style="left:382px"><span class="status-red">Accepting Players</span>&nbsp;&nbsp; Version : 584642 (R23)&nbsp;&nbsp; <span class="status-red">0.6.2.0</span></div>

<div class="abs tabs">
  <span style="padding:0 26px">Players</span><span>Chat</span><span>Map</span><span class="active">Events</span><span>Lists</span><span style="padding:0 26px">Server Settings</span><span style="padding:0 26px">Plugins</span><span style="padding:0 24px">Accounts</span><span>Console</span><span style="border:none;padding:0 28px">Parent Layer Control</span>
</div>

<div class="abs content"></div>

<section class="abs event-table">
  <div class="abs thead"></div>
  <div class="abs col-line" style="left:113px"></div>
  <div class="abs col-line" style="left:267px"></div>
  <div class="abs col-line" style="left:446px"></div>
  <div class="abs th" style="left:28px">Source</div>
  <div class="abs th" style="left:148px">Date and Time</div>
  <div class="abs th" style="left:297px">Event</div>
  <div class="abs th" style="left:499px">Message</div>
  <div class="abs" style="left:0;top:81px">
    <div class="abs row" style="top:0px"><span style="left:21px">Playerlist</span><span style="left:126px">10.24.2010&nbsp; 12:20:48</span><span style="left:277px">PlayerSwitchedSquads</span><span style="left:463px">Nightowlz swapped from squad Alpha to Charlie</span></div>
    <div class="abs row" style="top:30.6px"><span style="left:21px">Playerlist</span><span style="left:126px">10.24.2010&nbsp; 12:20:48</span><span style="left:277px">PlayerSwitchedSquads</span><span style="left:463px">Nightowlz swapped from squad Alpha to Charlie</span></div>
    <div class="abs row" style="top:61.2px"><span style="left:21px">Playerlist</span><span style="left:126px">10.24.2010&nbsp; 12:20:48</span><span style="left:277px">PlayerSwitchedSquads</span><span style="left:463px">Nightowlz swapped from squad Alpha to Charlie</span></div>
    <div class="abs row" style="top:91.8px"><span style="left:21px">Playerlist</span><span style="left:126px">10.24.2010&nbsp; 12:20:48</span><span style="left:277px">PlayerSwitchedSquads</span><span style="left:463px">Nightowlz swapped from squad Alpha to Charlie</span></div>
    <div class="abs row" style="top:122.4px"><span style="left:21px">Playerlist</span><span style="left:126px">10.24.2010&nbsp; 12:20:48</span><span style="left:277px">PlayerSwitchedSquads</span><span style="left:463px">Nightowlz swapped from squad Alpha to Charlie</span></div>
    <div class="abs row" style="top:153px"><span style="left:21px">Playerlist</span><span style="left:126px">10.24.2010&nbsp; 12:20:48</span><span style="left:277px">PlayerSwitchedSquads</span><span style="left:463px">Nightowlz swapped from squad Alpha to Charlie</span></div>
    <div class="abs row" style="top:183.6px"><span style="left:21px">Playerlist</span><span style="left:126px">10.24.2010&nbsp; 12:20:48</span><span style="left:277px">PlayerSwitchedSquads</span><span style="left:463px">Nightowlz swapped from squad Alpha to Charlie</span></div>
    <div class="abs row" style="top:214.2px"><span style="left:21px">Playerlist</span><span style="left:126px">10.24.2010&nbsp; 12:20:48</span><span style="left:277px">PlayerSwitchedSquads</span><span style="left:463px">Nightowlz swapped from squad Alpha to Charlie</span></div>
    <div class="abs row" style="top:244.8px"><span style="left:21px">Playerlist</span><span style="left:126px">10.24.2010&nbsp; 12:20:48</span><span style="left:277px">PlayerSwitchedSquads</span><span style="left:463px">Nightowlz swapped from squad Alpha to Charlie</span></div>
    <div class="abs row" style="top:275.4px"><span style="left:21px">Playerlist</span><span style="left:126px">10.24.2010&nbsp; 12:20:48</span><span style="left:277px">PlayerSwitchedSquads</span><span style="left:463px">Nightowlz swapped from squad Alpha to Charlie</span></div>
    <div class="abs row" style="top:306px"><span style="left:21px">Playerlist</span><span style="left:126px">10.24.2010&nbsp; 12:20:48</span><span style="left:277px">PlayerSwitchedSquads</span><span style="left:463px">Nightowlz swapped from squad Alpha to Charlie</span></div>
    <div class="abs row" style="top:336.6px"><span style="left:21px">Playerlist</span><span style="left:126px">10.24.2010&nbsp; 12:20:48</span><span style="left:277px">PlayerSwitchedSquads</span><span style="left:463px">Nightowlz swapped from squad Alpha to Charlie</span></div>
    <div class="abs row" style="top:367.2px"><span style="left:21px">Playerlist</span><span style="left:126px">10.24.2010&nbsp; 12:20:48</span><span style="left:277px">PlayerSwitchedSquads</span><span style="left:463px">Nightowlz swapped from squad Alpha to Charlie</span></div>
    <div class="abs row" style="top:397.8px"><span style="left:21px">Playerlist</span><span style="left:126px">10.24.2010&nbsp; 12:20:48</span><span style="left:277px">PlayerSwitchedSquads</span><span style="left:463px">Nightowlz swapped from squad Alpha to Charlie</span></div>
    <div class="abs row" style="top:428.4px"><span style="left:21px">Playerlist</span><span style="left:126px">10.24.2010&nbsp; 12:20:48</span><span style="left:277px">PlayerSwitchedSquads</span><span style="left:463px">Nightowlz swapped from squad Alpha to Charlie</span></div>
    <div class="abs row" style="top:459px"><span style="left:21px">Playerlist</span><span style="left:126px">10.24.2010&nbsp; 12:20:48</span><span style="left:277px">PlayerSwitchedSquads</span><span style="left:463px">Nightowlz swapped from squad Alpha to Charlie</span></div>
    <div class="abs row" style="top:489.6px"><span style="left:21px">Playerlist</span><span style="left:126px">10.24.2010&nbsp; 12:20:48</span><span style="left:277px">PlayerSwitchedSquads</span><span style="left:463px">Nightowlz swapped from squad Alpha to Charlie</span></div>
    <div class="abs row" style="top:520.2px"><span style="left:21px">Playerlist</span><span style="left:126px">10.24.2010&nbsp; 12:20:48</span><span style="left:277px">PlayerSwitchedSquads</span><span style="left:463px">Nightowlz swapped from squad Alpha to Charlie</span></div>
    <div class="abs row" style="top:550.8px"><span style="left:21px">Playerlist</span><span style="left:126px">10.24.2010&nbsp; 12:20:48</span><span style="left:277px">PlayerSwitchedSquads</span><span style="left:463px">Nightowlz swapped from squad Alpha to Charlie</span></div>
    <div class="abs row" style="top:581.4px"><span style="left:21px">Playerlist</span><span style="left:126px">10.24.2010&nbsp; 12:20:48</span><span style="left:277px">PlayerSwitchedSquads</span><span style="left:463px">Nightowlz swapped from squad Alpha to Charlie</span></div>
    <div class="abs row" style="top:612px"><span style="left:21px">Playerlist</span><span style="left:126px">10.24.2010&nbsp; 12:20:48</span><span style="left:277px">PlayerSwitchedSquads</span><span style="left:463px">Nightowlz swapped from squad Alpha to Charlie</span></div>
    <div class="abs row" style="top:642.6px"><span style="left:21px">Playerlist</span><span style="left:126px">10.24.2010&nbsp; 12:20:48</span><span style="left:277px">PlayerSwitchedSquads</span><span style="left:463px">Nightowlz swapped from squad Alpha to Charlie</span></div>
    <div class="abs row" style="top:673.2px"><span style="left:21px">Playerlist</span><span style="left:126px">10.24.2010&nbsp; 12:20:48</span><span style="left:277px">PlayerSwitchedSquads</span><span style="left:463px">Nightowlz swapped from squad Alpha to Charlie</span></div>
    <div class="abs row" style="top:703.8px"><span style="left:21px">Playerlist</span><span style="left:126px">10.24.2010&nbsp; 12:20:48</span><span style="left:277px">PlayerSwitchedSquads</span><span style="left:463px">Nightowlz swapped from squad Alpha to Charlie</span></div>
  </div>
</section>

<aside class="abs captures">
  <div class="abs cap-head">Captures</div>
  <div class="abs cap-close">Close</div>
  <div class="abs" style="left:0;top:42px;width:288px;height:776px;background:var(--panel)"></div>
  <div class="abs cap-label" style="top:60px">Maximum Captures</div>
  <div class="abs field" style="top:91px">100000
    <svg style="position:absolute;right:8px;top:7px" width="12" height="22" viewBox="0 0 12 22" fill="none" stroke="#333" stroke-width="2"><path d="M2 8 L6 3 L10 8"/><path d="M2 14 L6 19 L10 14"/></svg>
  </div>
  <div class="abs cap-label" style="top:152px">Events</div>
  <div class="abs field" style="top:173px">Playerloin</div>
  <svg class="abs" style="left:263px;top:185px" width="16" height="16" viewBox="0 0 16 16"><circle cx="8" cy="8" r="7" fill="#ccc" stroke="#999"/><path d="M8 4 V12 M4 8 H12" stroke="#fff" stroke-width="2"/></svg>
  <div class="abs cap-label" style="top:235px">Capturing Events</div>
  <div class="abs list">
    <div class="abs item" style="top:11px">Player loin</div>
    <div class="abs item" style="top:38px">Player Leave</div>
    <div class="abs item" style="top:65px">Player Killed</div>
    <div class="abs item" style="top:92px">Ip Kicked</div>
    <div class="abs item" style="top:119px">Player Timed Banned</div>
    <div class="abs item" style="top:146px">Player Unbanned</div>
    <div class="abs item" style="top:173px">IP Time Banned</div>
    <div class="abs item" style="top:200px">IP Round Banned</div>
    <div class="abs item" style="top:228px">GUID Timed Banned</div>
    <div class="abs item" style="top:255px">GUID Permanent Banned</div>
    <div class="abs item" style="top:282px">GUID Round Banned</div>
    <div class="abs item" style="top:309px">Level Loading</div>
    <div class="abs item" style="top:336px">Player loin</div>
    <div class="abs item" style="top:363px">Player Leave</div>
    <div class="abs item" style="top:390px">Player Killed</div>
    <div class="abs item" style="top:418px">Ip Kicked</div>
    <div class="abs item" style="top:445px">Player Timed Banned</div>
    <div class="abs vscroll"><div class="abs" style="left:4px;top:34px;width:14px;height:26px;background:#bbb"></div></div>
    <div class="abs hscroll"><div class="abs" style="left:38px;top:3px;width:26px;height:12px;background:#bbb"></div></div>
  </div>
  <div class="abs btn">Clear Eventlist</div>
</aside>
</body>
</html>
```